Update Product Descriptions on Existing Website

We need to update product descriptions and images on three pages of our existing website. The tables are in editable HTML format. The formatting will be the exact same, just need the descriptions and images updated.

I have included the source documents below.

Coding

Coded - Design and coding required

Number of Pages Required

3 page

Colors

Designer to choose colors to be used in the design.

```html
<!DOCTYPE html>
<html lang="en">
<head>
<meta charset="utf-8">
<title>Pultruded Grating Sizes and Types</title>
<link rel="stylesheet" href="https://fonts.googleapis.com/css2?family=Tinos:wght@400&display=swap">
<style>
  :root {
    --page-bg: #ffffff;
    --ink: #000000;
    --rule: #2b2b2b;
    --grating-light: #4fb36a;
    --grating-mid: #2f9a4f;
    --grating-dark: #1f7a3b;
  }
  * { box-sizing: border-box; margin: 0; padding: 0; }
  html, body {
    width: 1200px;
    height: 2243px;
    overflow: hidden;
    background: var(--page-bg);
  }
  body {
    font-family: "Tinos", "Times New Roman", serif;
    font-size: 26px;
    color: var(--ink);
  }
  .intro {
    position: absolute;
    left: 13px;
    top: 6px;
    line-height: 34px;
  }
  .grating-table {
    position: absolute;
    left: 13px;
    top: 46px;
    width: 1176px;
    table-layout: fixed;
    border-collapse: separate;
    border-spacing: 2px;
    border: 1px solid var(--rule);
  }
  .grating-table td {
    border: 1px solid var(--rule);
    padding: 0 2px;
    line-height: 28px;
    height: 30px;
    vertical-align: middle;
    white-space: nowrap;
    overflow: hidden;
  }
  .grating-table .label-col { width: 337px; }
  .profile-row td { height: 167px; }
  .profile-cell { text-align: center; }
  .profile-render {
    display: inline-block;
    width: 180px;
    height: 130px;
    vertical-align: middle;
    border-radius: 6px;
    background: linear-gradient(135deg, var(--grating-light), var(--grating-mid) 55%, var(--grating-dark));
  }
  .empty-cell { border: 1px solid var(--rule); }
</style>
</head>
<body>
  <p class="intro">The following sizes and types of pultruded grating are available from KPG:</p>

  <table class="grating-table">
    <colgroup>
      <col class="label-col">
      <col><col><col><col>
    </colgroup>
    <tbody>
      <!-- Block 1 -->
      <tr class="profile-row">
        <td>Profile Image (click to enlarge)</td>
        <td class="profile-cell"><span class="profile-render" role="img" aria-label="Green pultruded grating profile T4010"></span></td>
        <td class="profile-cell"><span class="profile-render" role="img" aria-label="Green pultruded grating profile T5010"></span></td>
        <td class="profile-cell"><span class="profile-render" role="img" aria-label="Green pultruded grating profile T6010"></span></td>
        <td class="profile-cell"><span class="profile-render" role="img" aria-label="Green pultruded grating profile I4010"></span></td>
      </tr>
      <tr><td>Type</td><td>T4010</td><td>T5010</td><td>T6010</td><td>I4010</td></tr>
      <tr><td>Height (in.)</td><td>1</td><td>1</td><td>1</td><td>1</td></tr>
      <tr><td>Standard Panel Width (ft.)</td><td>3,4</td><td>3,4</td><td>3,4</td><td>3,4</td></tr>
      <tr><td>Standard Panel Length (ft.)</td><td>8,10,12,20</td><td>8,10,12,20</td><td>8,10,12,20</td><td>8,10,12,20</td></tr>
      <tr><td>Open Area</td><td>40%</td><td>50%</td><td></td><td>40%</td></tr>
      <tr><td>Weight (lbs./ft.)</td><td>2.46</td><td>2.15</td><td>1.74</td><td>3.28</td></tr>

      <!-- Block 2 -->
      <tr class="profile-row">
        <td>Profile Image (click to enlarge)</td>
        <td class="profile-cell"><span class="profile-render" role="img" aria-label="Green pultruded grating profile I5010"></span></td>
        <td class="profile-cell"><span class="profile-render" role="img" aria-label="Green pultruded grating profile I6010"></span></td>
        <td class="profile-cell"><span class="profile-render" role="img" aria-label="Green pultruded grating profile I4012"></span></td>
        <td class="profile-cell"><span class="profile-render" role="img" aria-label="Green pultruded grating profile II5012"></span></td>
      </tr>
      <tr><td>Type</td><td>I5010</td><td>I6010</td><td>I4012</td><td>II5012</td></tr>
      <tr><td>Height (in.)</td><td>1</td><td>1</td><td>1.25</td><td>1.25</td></tr>
      <tr><td>Standard Panel Width (ft.)</td><td>3,4</td><td>3,4</td><td>3,4</td><td>3,4</td></tr>
      <tr><td>Standard Panel Length (ft.)</td><td>8,10,12,20</td><td>8,10,12,20</td><td>8,10,12,20</td><td>8,10,12,20</td></tr>
      <tr><td>Open Area</td><td>50%</td><td>60%</td><td>40%</td><td>50%</td></tr>
      <tr><td>Weight (lbs./ft.)</td><td>2.74</td><td>2.21</td><td>4.12</td><td>3.48</td></tr>

      <!-- Block 3 -->
      <tr class="profile-row">
        <td>Profile Image (click to enlarge)</td>
        <td class="profile-cell"><span class="profile-render" role="img" aria-label="Green pultruded grating profile I6012"></span></td>
        <td class="profile-cell"><span class="profile-render" role="img" aria-label="Green pultruded grating profile I4015"></span></td>
        <td class="profile-cell"><span class="profile-render" role="img" aria-label="Green pultruded grating profile I5015"></span></td>
        <td class="profile-cell"><span class="profile-render" role="img" aria-label="Green pultruded grating profile I6015"></span></td>
      </tr>
      <tr><td>Type</td><td>I6012</td><td>I4015</td><td>I5015</td><td>I6015</td></tr>
      <tr><td>Height (in.)</td><td>1.25</td><td>1.5</td><td>1.5</td><td>1.5</td></tr>
      <tr><td>Standard Panel Width (ft.)</td><td>3,4</td><td>3,4</td><td>3,4</td><td>3,4</td></tr>
      <tr><td>Standard Panel Length (ft.)</td><td>8,10,12,20</td><td>8,10,12,20</td><td>8,10,12,20</td><td>8,10,12,20</td></tr>
      <tr><td>Open Area</td><td>60%</td><td>40%</td><td>50%</td><td>60%</td></tr>
      <tr><td>Weight (lbs./ft.)</td><td>2.89</td><td>5.33</td><td>4.57</td><td>3.71</td></tr>

      <!-- Block 4 -->
      <tr class="profile-row">
        <td>Profile Image (click to enlarge)</td>
        <td class="profile-cell"><span class="profile-render" role="img" aria-label="Green pultruded grating profile T3320"></span></td>
        <td class="profile-cell"><span class="profile-render" role="img" aria-label="Green pultruded grating profile T5020"></span></td>
        <td class="profile-cell"><span class="profile-render" role="img" aria-label="Green pultruded grating profile T3330"></span></td>
        <td class="profile-cell"><span class="profile-render" role="img" aria-label="Green pultruded grating profile T5030"></span></td>
      </tr>
      <tr><td>Type</td><td>T3320</td><td>T5020</td><td>T3330</td><td>T5030</td></tr>
      <tr><td>Height (in.)</td><td>2</td><td>2</td><td>3</td><td>3</td></tr>
      <tr><td>Standard Panel Width (ft.)</td><td>3,4</td><td>3,4</td><td>3,4</td><td>3,4</td></tr>
      <tr><td>Standard Panel Length (ft.)</td><td>8,10,12,20</td><td>8,10,12,20</td><td>8,10,12,20</td><td>8,10,12,20</td></tr>
      <tr><td>Open Area</td><td>33%</td><td>50%</td><td>33%</td><td>50%</td></tr>
      <tr><td>Weight (lbs./ft.)</td><td>4.63</td><td>3.56</td><td>5.21</td><td>6.8</td></tr>

      <!-- Block 5 -->
      <tr class="profile-row">
        <td>Profile Image (click to enlarge)</td>
        <td class="profile-cell"><span class="profile-render" role="img" aria-label="Green pultruded grating profile T3320"></span></td>
        <td class="profile-cell"><span class="profile-render" role="img" aria-label="Green pultruded grating profile HD I 4020"></span></td>
        <td class="profile-cell"><span class="profile-render" role="img" aria-label="Green pultruded grating profile HD I 5020"></span></td>
        <td class="profile-cell"><span class="profile-render" role="img" aria-label="Green pultruded grating profile HD I 6020"></span></td>
      </tr>
      <tr><td>Type</td><td>T3320</td><td>HD I 4020</td><td>HD I 5020</td><td>HD I 6020</td></tr>
      <tr><td>Height (in.)</td><td>2</td><td>2</td><td>2</td><td>2</td></tr>
      <tr><td>Standard Panel Width (ft.)</td><td>3,4</td><td>3,4</td><td>3,4</td><td>3,4</td></tr>
      <tr><td>Standard Panel Length (ft.)</td><td>8,10,12,20</td><td>8,10,12,20</td><td>8,10,12,20</td><td>8,10,12,20</td></tr>
      <tr><td>Open Area</td><td>33%</td><td>40%</td><td>50%</td><td>60%</td></tr>
      <tr><td>Weight (lbs./ft.)</td><td>4.6</td><td>11.7</td><td>9.8</td><td>7.8</td></tr>

      <!-- Block 6 -->
      <tr class="profile-row">
        <td>Profile Image (click to enlarge)</td>
        <td class="profile-cell"><span class="profile-render" role="img" aria-label="Green pultruded grating profile HD I 7020"></span></td>
        <td class="profile-cell"><span class="profile-render" role="img" aria-label="Green pultruded grating profile T 5030"></span></td>
        <td class="profile-cell"><span class="profile-render" role="img" aria-label="Green pultruded grating profile T 3330"></span></td>
        <td class="empty-cell" rowspan="7"></td>
      </tr>
      <tr><td>Type</td><td>HD I 7020</td><td>T 5030</td><td>T 3330</td></tr>
      <tr><td>Height (in.)</td><td>2</td><td>3</td><td>3</td></tr>
      <tr><td>Standard Panel Width (ft.)</td><td>3,4</td><td>3,4</td><td>3,4</td></tr>
      <tr><td>Standard Panel Length (ft.)</td><td>8,10,12,20</td><td>8,10,12,20</td><td>8,10,12,20</td></tr>
      <tr><td>Open Area</td><td>70%</td><td>50%</td><td>33%</td></tr>
      <tr><td>Weight (lbs./ft.)</td><td>6.3</td><td>5.3</td><td>6.5</td></tr>
    </tbody>
  </table>
</body>
</html>
```